Harrow Bend Family Law magazine ad

I need an ad that will run in Marlow Creek Living Magazine here in NC. The ad will be a 1/2 page ad, (7.25X4.875). Resolution is 300 dpi or higher.

We are a family law firm (divorce) and we want to high light child custody issues. I would like the ad copy to include our logo (which you can find on our website www.harrowbendfamilylaw.com) and I can send a high res one if you are chosen. Ad MUST include our address and phone number by state law.

Ad copy will be something about protecting children (something brief) like "Protect what you love" or something like that. I will pick quick as I have to turn it in on Wednesday. You will need to be able to email the final product to graphics@marlowcreeklivingmag.com and me too.

Target Market(s)

Married couples with kids (primarily men) ages 35-50

Industry/Entity Type

Legal

Colors
85cae6
cadf82
fbee3f
fbf289
33a6d7
33b8a4
add136

Requirements
Must have
• website, logo, address, and phone number
Nice to have
• creative and heart provoking (I want the image to make me want to act)
Should not have
• Don't be boring or give me some stock photo I have seen in a million divorce ads.

```html
<!DOCTYPE html>
<html lang="en">
<head>
<meta charset="utf-8">
<title>Harrow Bend Family Law – Protect what you love</title>
<link rel="stylesheet" href="https://fonts.googleapis.com/css2?family=Quicksand:wght@500;600;700&display=swap">
<style>
  :root {
    --wall-light: #c3ccd1;
    --wall-mid: #98a3aa;
    --wall-dark: #5e676d;
    --corner-shadow: #2f3437;
    --hair: #3a3331;
    --skin: #a8998f;
    --shirt: #b39c9d;
    --shirt-shade: #8e7b7d;
    --waist: #3c3d43;
    --skirt: #8c8d92;
    --legs: #a59b95;
    --floor: #6d767c;
    --ink: #3b3838;
    --paper: #f2f4f5;
    --paper-soft: #e6eaec;
    --brand-blue: #33a6d7;
    --brand-teal: #33b8a4;
    --pin-green: #7cc242;
    --phone-blue: #2f7fc0;
  }
  html, body {
    margin: 0;
    padding: 0;
    width: 1200px;
    height: 807px;
    overflow: hidden;
    background: #ffffff;
  }
  .ad {
    position: relative;
    width: 1200px;
    height: 807px;
    overflow: hidden;
    font-family: "Quicksand", sans-serif;
  }
  .ad__wall {
    position: absolute;
    inset: 0;
    background:
      linear-gradient(90deg, var(--corner-shadow) 0%, var(--wall-dark) 9%, rgba(94,103,109,0) 22%),
      linear-gradient(0deg, var(--floor) 0%, rgba(109,118,124,0) 22%),
      radial-gradient(ellipse at 70% 38%, var(--wall-light) 0%, var(--wall-mid) 58%, var(--wall-dark) 100%);
  }
  .ad__child {
    position: absolute;
    left: 80px;
    top: 62px;
    width: 440px;
    height: 730px;
    border-radius: 46% 46% 30% 30% / 24% 24% 12% 12%;
    background:
      linear-gradient(180deg,
        var(--hair) 0%,
        var(--hair) 22%,
        var(--skin) 30%,
        var(--shirt) 40%,
        var(--shirt-shade) 62%,
        var(--waist) 70%,
        var(--skirt) 78%,
        var(--legs) 90%,
        var(--floor) 100%);
    -webkit-mask-image: radial-gradient(ellipse 55% 55% at 50% 50%, #000 70%, transparent 100%);
    mask-image: radial-gradient(ellipse 55% 55% at 50% 50%, #000 70%, transparent 100%);
  }
  .brand {
    position: absolute;
    left: 86px;
    top: 58px;
    display: flex;
    align-items: center;
    gap: 12px;
  }
  .brand__dot {
    width: 64px;
    height: 64px;
    border-radius: 50%;
    background: var(--brand-teal);
  }
  .brand__name {
    font-weight: 700;
    font-size: 23px;
    line-height: 1.1;
    color: var(--brand-blue);
    width: 130px;
  }
  .phone {
    position: absolute;
    left: 782px;
    top: 70px;
    display: flex;
    align-items: center;
    gap: 10px;
  }
  .phone__number {
    font-weight: 700;
    font-size: 45px;
    color: var(--paper);
    letter-spacing: 0;
  }
  .headline {
    position: absolute;
    left: 496px;
    top: 158px;
    margin: 0;
    color: var(--ink);
    font-weight: 600;
    line-height: 1;
  }
  .headline__line { display: block; white-space: nowrap; }
  .headline__protect { font-size: 130px; letter-spacing: -1px; }
  .headline__what { font-size: 92px; margin-left: 54px; margin-top: -14px; }
  .headline__love { font-size: 336px; letter-spacing: -4px; margin-top: -104px; margin-left: -6px; line-height: 0.9; }
  .website {
    position: absolute;
    left: 574px;
    top: 586px;
    font-weight: 600;
    font-size: 31.5px;
    color: var(--paper);
  }
  .address {
    position: absolute;
    left: 500px;
    top: 670px;
    display: flex;
    align-items: flex-start;
    gap: 26px;
  }
  .address__text {
    margin: 4px 0 0;
    font-style: normal;
    font-weight: 600;
    font-size: 29px;
    line-height: 1.22;
    color: var(--paper-soft);
  }
</style>
</head>
<body>
<main class="ad">
  <div class="ad__wall"></div>
  <div class="ad__child" role="img" aria-label="Photo of a young girl with long dark hair in a pink top and striped skirt, kneeling in the corner of a bare grey room with her hands over her eyes"></div>

  <div class="brand">
    <span class="brand__dot"></span>
    <span class="brand__name">Harrow Bend Family Law</span>
  </div>

  <div class="phone">
    <svg width="38" height="52" viewBox="0 0 38 52" aria-hidden="true">
      <rect x="6" y="2" width="26" height="48" rx="4" fill="#222" transform="rotate(12 19 26)"/>
      <rect x="9" y="8" width="20" height="34" rx="1.5" fill="var(--phone-blue)" transform="rotate(12 19 26)"/>
    </svg>
    <span class="phone__number">555.014.0362</span>
  </div>

  <h1 class="headline">
    <span class="headline__line headline__protect">Protect</span>
    <span class="headline__line headline__what">what you</span>
    <span class="headline__line headline__love">love</span>
  </h1>

  <div class="website">www.harrowbendfamilylaw.com</div>

  <div class="address">
    <svg width="48" height="62" viewBox="0 0 48 62" aria-hidden="true">
      <path d="M24 60 C24 60 4 36 4 22 A20 20 0 0 1 44 22 C44 36 24 60 24 60 Z" fill="var(--pin-green)"/>
      <circle cx="24" cy="22" r="8" fill="#3f7a1f"/>
    </svg>
    <address class="address__text">4120 Larkspur Avenue, Suite 208,<br>Alder Point, NC 28519</address>
  </div>
</main>
</body>
</html>
```